New modern website for Kerbline Groundworks

Hi we are an existing company that has a current website http://www.kerblinegroundworks.co.nz/ we are looking to get a new vibrant looking website designed to take us further and gain more customers. We are after a simple easy to use website that does not confuse but we want to make an impact and stand out from the rest

Target Market(s)

Homeowners And Commercial Businesses

Industry/Entity Type

It Company

Coding

Coded - Design and coding required

Number of Pages Required

2 page

```html
<!DOCTYPE html>
<html lang="en">
<head>
<meta charset="utf-8">
<title>Kerbline Groundworks</title>
<link href="https://fonts.googleapis.com/css2?family=Raleway:wght@300;400;500;600;700&display=swap" rel="stylesheet">
<style>
:root{
  --red:#e01b1b;
  --ink:#333333;
  --muted:#666666;
  --band:#efeded;
  --white:#ffffff;
  --footer:#1d1d1d;
  --footer-line:#3a3a3a;
  --footer-text:#cfcfcf;
}
*{box-sizing:border-box;margin:0;padding:0}
html,body{width:1200px;height:3409px;overflow:hidden}
body{font-family:"Raleway",sans-serif;color:var(--ink);background:var(--white)}
.page{position:relative;width:1200px;height:3409px;overflow:hidden}

/* header */
.site-header{height:89px;display:flex;align-items:center;justify-content:space-between;padding:0 80px}
.brand{display:flex;align-items:center;gap:12px}
.brand-mark{width:22px;height:22px;background:var(--ink)}
.brand-name{font-size:24px;font-weight:700;letter-spacing:1px;color:var(--ink);text-transform:uppercase}
.main-nav{display:flex;gap:28px}
.main-nav a{font-size:15px;color:var(--ink);text-decoration:none;text-transform:uppercase}

/* hero */
.hero{position:relative;height:541px;background:linear-gradient(180deg,#a9c3d4 0%,#6d8a6a 30%,#3d5233 60%,#8a8780 80%,#bdb7ad 100%);display:flex;align-items:center;justify-content:center}
.hero h1{color:var(--white);font-size:44px;font-weight:600;text-align:center;line-height:1.3;text-transform:uppercase;text-shadow:0 2px 6px rgba(0,0,0,.4)}
.hero-shadow{height:22px;background:radial-gradient(ellipse at top,rgba(0,0,0,.22),rgba(0,0,0,0) 70%)}

.section-title{font-size:42px;font-weight:300;text-transform:uppercase;text-align:center;color:var(--ink);letter-spacing:1px}
.section-title .accent{color:var(--red)}

.btn{display:inline-block;background:var(--red);color:var(--white);font-size:13px;text-decoration:none;text-align:center}

/* welcome */
.welcome{height:356px;padding-top:48px;text-align:center}
.welcome p{width:1028px;margin:46px auto 0;font-size:13.5px;line-height:23px;color:var(--muted)}
.welcome .btn{width:160px;height:45px;line-height:45px;margin-top:24px}

/* services */
.services{height:580px;background:var(--band);padding-top:56px}
.service-cards{display:flex;justify-content:center;gap:27px;margin-top:44px}
.service-card{width:330px;height:363px;background:var(--white);text-align:center}
.service-photo{height:164px}
.service-card h3{font-size:26px;font-weight:400;text-transform:uppercase;margin-top:22px}
.service-card p{font-size:12.5px;line-height:19px;color:var(--muted);padding:0 22px;margin-top:10px}
.service-card .btn{width:94px;height:29px;line-height:29px;font-size:11.5px;margin-top:14px}

/* why choose us */
.why{height:454px;padding-top:48px}
.features{display:flex;justify-content:center;margin-top:42px}
.feature{width:268px;text-align:center}
.feature-icon{width:110px;height:110px;margin:0 auto;border-radius:50%;border:5px solid var(--red);background:#2b2b2b;display:flex;align-items:center;justify-content:center}
.feature h3{font-size:21px;font-weight:400;text-transform:uppercase;margin-top:28px}
.feature p{font-size:12.5px;line-height:19px;color:var(--muted);padding:0 40px;margin-top:12px}

/* projects */
.projects{height:232px;background:var(--band);padding-top:56px;text-align:center}
.projects p{width:1000px;margin:28px auto 0;font-size:13px;line-height:21px;color:var(--muted)}
.gallery{position:relative;height:268px;display:flex}
.gallery-item{width:357px;height:268px;flex:none}
.gallery-item.partial{width:129px}
.g1{background:linear-gradient(180deg,#cfd6dc 0%,#9aa19a 45%,#3a3d3f 100%)}
.g2{background:linear-gradient(180deg,#b98585 0%,#a46a66 55%,#8d5c58 100%)}
.g3{background:linear-gradient(180deg,#6b7560 0%,#4f5048 50%,#2f3132 100%)}
.g4{background:linear-gradient(180deg,#c8c8c0 0%,#7f7b72 50%,#3b3b3b 100%)}
.gallery-arrow{position:absolute;top:112px;width:44px;height:44px;border-radius:50%;background:rgba(0,0,0,.35);display:flex;align-items:center;justify-content:center}
.gallery-arrow.prev{left:84px}
.gallery-arrow.next{right:84px}

/* testimonials */
.testimonials{height:455px;padding-top:52px}
.quotes{display:flex;justify-content:center;gap:36px;margin-top:42px}
.quote{position:relative;width:490px;height:138px;border:3px solid #2f2f2f;border-radius:6px;padding:18px 120px 0 20px}
.quote::before{content:"\201C";position:absolute;left:14px;top:-14px;font-size:90px;color:#e2e2e2;line-height:1}
.quote p{position:relative;font-size:11.5px;line-height:17px;color:var(--ink)}
.quote .name{font-size:12px;font-weight:700;margin-top:14px}
.quote .role{font-size:11px;color:var(--muted)}
.avatar{position:absolute;right:22px;bottom:-44px;width:96px;height:96px;border-radius:50%;border:4px solid var(--red);background:linear-gradient(180deg,#d9d4cf,#9a9590)}

/* footer */
.site-footer{height:413px;background:var(--footer);color:var(--footer-text);position:relative}
.footer-brand{display:flex;justify-content:center;align-items:center;gap:12px;padding-top:28px}
.footer-brand .brand-mark{background:var(--white)}
.footer-brand .brand-name{color:var(--white)}
.footer-cols{position:absolute;top:134px;left:80px;right:79px;display:flex}
.footer-col h4{font-size:13px;font-weight:600;color:var(--red);text-transform:uppercase;padding-bottom:8px;border-bottom:1px solid var(--footer-line)}
.col-links{width:150px;margin-right:28px}
.col-news{width:218px;margin-right:50px}
.col-contact{width:234px;margin-right:32px}
.col-links ul{list-style:none;margin-top:12px}
.col-links li{font-size:11.5px;line-height:25px;text-transform:uppercase}
.col-links li::before{content:"\203A";margin-right:8px}
.col-news p{font-size:11.5px;line-height:16px;margin-top:14px}
.email-field{width:206px;height:26px;background:var(--white);margin-top:12px;color:#999;font-size:10.5px;padding:6px 8px}
.col-news .btn{width:72px;height:22px;line-height:22px;font-size:10px;margin-top:14px}
.contact-line{display:flex;gap:12px;font-size:11.5px;line-height:16px;margin-top:14px}
.contact-line svg{flex:none;margin-top:1px}
.map{width:330px;height:114px;margin-top:26px;background:linear-gradient(135deg,#e8e6df,#cfd8c8 60%,#d9dce2)}
.footer-bottom{position:absolute;left:80px;right:79px;bottom:30px;display:flex;align-items:center;justify-content:space-between}
.follow{display:flex;align-items:center;gap:8px}
.follow span{font-size:12px;font-weight:600;color:var(--red);text-transform:uppercase;margin-right:10px}
.social-box{width:28px;height:28px;background:#4a7fb7}
.social-box.alt1{background:#e57a2c}
.social-box.alt2{background:#3b5998}
.social-box.alt3{background:#cc2222}
.social-box.alt4{background:#3f6fd8}
.copyright{font-size:11.5px}
</style>
</head>
<body>
<div class="page">

  <header class="site-header">
    <div class="brand"><span class="brand-mark"></span><span class="brand-name">Kerbline Groundworks</span></div>
    <nav class="main-nav">
      <a href="#">Home</a><a href="#">About</a><a href="#">Services</a><a href="#">Projects</a><a href="#">Contact Us</a>
    </nav>
  </header>

  <section class="hero" role="img" aria-label="Winding asphalt mountain road lined with pine trees and a guard rail">
    <h1>Setting the standards for quality<br>concrete &amp; asphalters</h1>
  </section>
  <div class="hero-shadow"></div>

  <section class="welcome">
    <h2 class="section-title">Welcome</h2>
    <p>Suspendisse aliquet lacus in elementum venenatis. Suspendisse quis hendrerit lacus. Sed ac egestas ligula. Nam consequat massa a erat varius molestie. Sed velit risus, porttitor et nisi sed, suscipit molestie tellus. In erat metus, convallis et sem sed, rutrum rutrum nibh. Nullam vestibulum, dui et tristique venenatis, velit lectus volutpat tortor, euismod porta metus odio et urna. Curabitur vel vehicula leo. Etiam lacus sem, efficitur a nisl dictum, bibendum ullamcorper purus. Donec massa tellus, scelerisque vel velit eget, pretium viverra libero. Proin urna ex, consequat non mauris id, pharetra porta lorem. Proin eros est, rhoncus sed ante sit amet, iaculis bibendum mauris. Nulla vulputate nulla dolor, suscipit vehicula lorem commodo in.</p>
    <a class="btn" href="#">Read More...</a>
  </section>

  <section class="services">
    <h2 class="section-title">We are here to fulfill <span class="accent">&ldquo;Your Requirement&rdquo;</span></h2>
    <div class="service-cards">
      <article class="service-card">
        <div class="service-photo" role="img" aria-label="Road crew laying fresh asphalt with a roller" style="background:linear-gradient(180deg,#8a8d8c,#4c4f52 60%,#2e3033)"></div>
        <h3>Asphalt</h3>
        <p>Quisque facilisis vulputate turpis et suscipit. Quisque tincidunt nisi sed lorem placerat auctor. Praesent posuere tortor eget metus rutrum vehicula. Aenean quis ultrices nisi. Etiam nulla nibh.</p>
        <a class="btn" href="#">Learn More</a>
      </article>
      <article class="service-card">
        <div class="service-photo" role="img" aria-label="Paved concrete driveway bordered by trees" style="background:linear-gradient(180deg,#9fbf88,#6f8d5c 45%,#b9b4ab 70%,#9c968d)"></div>
        <h3>Concrete</h3>
        <p>Quisque facilisis vulputate turpis et suscipit. Quisque tincidunt nisi sed lorem placerat auctor. Praesent posuere tortor eget metus rutrum vehicula. Aenean quis ultrices nisi. Etiam nulla nibh.</p>
        <a class="btn" href="#">Learn More</a>
      </article>
      <article class="service-card">
        <div class="service-photo" role="img" aria-label="New house with a concrete driveway and garage" style="background:linear-gradient(180deg,#9fc2e0,#d8dadc 45%,#c4bfb6 75%,#a9a49a)"></div>
        <h3>Additional Services</h3>
        <p>Quisque facilisis vulputate turpis et suscipit. Quisque tincidunt nisi sed lorem placerat auctor. Praesent posuere tortor eget metus rutrum vehicula. Aenean quis ultrices nisi. Etiam nulla nibh.</p>
        <a class="btn" href="#">Learn More</a>
      </article>
    </div>
  </section>

  <section class="why">
    <h2 class="section-title">Why choose us ?</h2>
    <div class="features">
      <div class="feature">
        <div class="feature-icon">
          <svg width="50" height="50" viewBox="0 0 50 50" fill="none" stroke="#fff" stroke-width="4"><circle cx="25" cy="22" r="8"/><path d="M25 6v6M25 32v6M9 22h6M35 22h6M14 11l4 4M32 29l4 4M36 11l-4 4M18 29l-4 4"/><path d="M6 44c8-6 14-2 20-2h12" stroke-linecap="round"/></svg>
        </div>
        <h3>Full Service</h3>
        <p>Nulla eu dictum metus. Cras eleifend justo tellus, ut scelerisque justo luctus id. Cras lacinia pharetra nulla sed Dulla cat zebra little ullamcorper.</p>
      </div>
      <div class="feature">
        <div class="feature-icon">
          <svg width="46" height="46" viewBox="0 0 24 24" fill="#fff"><path d="M12 2l2.9 6.6 7.1.6-5.4 4.7 1.7 7L12 17.3 5.7 20.9l1.7-7L2 9.2l7.1-.6z"/></svg>
        </div>
        <h3>Experienced</h3>
        <p>Nulla eu dictum metus. Cras eleifend justo tellus, ut scelerisque justo luctus id. Cras lacinia pharetra nulla sed Dulla cat zebra little ullamcorper.</p>
      </div>
      <div class="feature">
        <div class="feature-icon">
          <svg width="40" height="52" viewBox="0 0 40 52" fill="#fff"><circle cx="20" cy="7" r="6"/><path d="M10 16h20l3 18h-6v18h-5V36h-4v16h-5V34H7z"/></svg>
        </div>
        <h3>Professional</h3>
        <p>Nulla eu dictum metus. Cras eleifend justo tellus, ut scelerisque justo luctus id. Cras lacinia pharetra nulla sed Dulla cat zebra little ullamcorper.</p>
      </div>
      <div class="feature">
        <div class="feature-icon">
          <svg width="44" height="50" viewBox="0 0 44 50"><path d="M22 2l18 7v14c0 12-8 21-18 25C12 44 4 35 4 23V9z" fill="#fff"/><path d="M13 25l6 6 12-12" fill="none" stroke="#2b2b2b" stroke-width="4"/></svg>
        </div>
        <h3>Insured</h3>
        <p>Nulla eu dictum metus. Cras eleifend justo tellus, ut scelerisque justo luctus id. Cras lacinia pharetra nulla sed Dulla cat zebra little ullamcorper.</p>
      </div>
    </div>
  </section>

  <section class="projects">
    <h2 class="section-title">Projects that <span class="accent">proves our strength</span></h2>
    <p>Lorem ipsum dolor sit amet, consectetur adipiscing elit. Praesent rutrum sem quam, vel dignissim lacus placerat quis. Nunc et turpis nec massa vulputate efficitur ut. Proin accumsan at massa eget dapibus. Ut sollicitudin id est non auctor. Praesent ut tincidunt elit.</p>
  </section>
  <div class="gallery">
    <div class="gallery-item g1" role="img" aria-label="Finished asphalt driveway in front of a white house"></div>
    <div class="gallery-item g2" role="img" aria-label="Crew screeding wet concrete on site"></div>
    <div class="gallery-item g3" role="img" aria-label="Sealed path beside a stone retaining wall"></div>
    <div class="gallery-item g4 partial" role="img" aria-label="Residential driveway project"></div>
    <span class="gallery-arrow prev"><svg width="14" height="20" viewBox="0 0 14 20"><path d="M11 2L3 10l8 8" fill="none" stroke="#fff" stroke-width="3"/></svg></span>
    <span class="gallery-arrow next"><svg width="14" height="20" viewBox="0 0 14 20"><path d="M3 2l8 8-8 8" fill="none" stroke="#fff" stroke-width="3"/></svg></span>
  </div>

  <section class="testimonials">
    <h2 class="section-title">Testimonials</h2>
    <div class="quotes">
      <blockquote class="quote">
        <p>Lorem ipsum dolor sit amet, consectetur adipiscing elit. Nulla fermentum dignissim risus eleifend sagittis. Integer turpis mi, hendrerit a leo eu, vestibulum dictum sem. Nullam egestas mauris in dui cursus, nec porta lectus tempus.</p>
        <p class="name">Tom Bradley</p>
        <p class="role">Customer</p>
        <span class="avatar" role="img" aria-label="Customer portrait"></span>
      </blockquote>
      <blockquote class="quote">
        <p>Lorem ipsum dolor sit amet, consectetur adipiscing elit. Nulla fermentum dignissim risus eleifend sagittis. Integer turpis mi, hendrerit a leo eu, vestibulum dictum sem. Nullam egestas mauris in dui cursus, nec porta lectus tempus.</p>
        <p class="name">Rachel Hart</p>
        <p class="role">Customer</p>
        <span class="avatar" role="img" aria-label="Customer portrait"></span>
      </blockquote>
    </div>
  </section>

  <footer class="site-footer">
    <div class="footer-brand"><span class="brand-mark"></span><span class="brand-name">Kerbline Groundworks</span></div>
    <div class="footer-cols">
      <div class="footer-col col-links">
        <h4>Quick Links</h4>
        <ul><li>Home</li><li>About Us</li><li>Services</li><li>Projects Gallery</li><li>Contact Us</li></ul>
      </div>
      <div class="footer-col col-news">
        <h4>Newsletter Signup</h4>
        <p>Please enter your email address below to receive our FREE newsletter</p>
        <div class="email-field">Your Email ID</div>
        <a class="btn" href="#">Subscribe</a>
      </div>
      <div class="footer-col col-contact">
        <h4>Contact Information</h4>
        <div class="contact-line"><svg width="10" height="14" viewBox="0 0 10 14"><path d="M5 0a5 5 0 015 5c0 4-5 9-5 9S0 9 0 5a5 5 0 015-5z" fill="#cfcfcf"/><circle cx="5" cy="5" r="2" fill="#1d1d1d"/></svg><span>14 Harbour Lane 2331 Westfield,<br>New Zealand</span></div>
        <div class="contact-line"><svg width="10" height="14" viewBox="0 0 10 14"><path d="M2 0h3l1 4-2 1c.5 2 1.5 3.5 3 4.5l1.5-1.5L10 10v3l-1 1C4 14 0 8 0 2z" fill="#cfcfcf"/></svg><span>+64 (09) 555 0142</span></div>
        <div class="contact-line"><svg width="12" height="10" viewBox="0 0 12 10"><rect width="12" height="10" fill="#cfcfcf"/><path d="M0 0l6 5 6-5" fill="none" stroke="#1d1d1d" stroke-width="1.2"/></svg><span>info@kerblinegroundworks.co.nz</span></div>
      </div>
      <div class="map" role="img" aria-label="Street map showing the office location"></div>
    </div>
    <div class="footer-bottom">
      <div class="follow"><span>Follow Us</span><i class="social-box"></i><i class="social-box alt1"></i><i class="social-box alt2"></i><i class="social-box alt3"></i><i class="social-box alt4"></i></div>
      <p class="copyright">Copyright 2016@kerblinegroundworks.co.nz, All Rights Reserved.</p>
    </div>
  </footer>

</div>
</body>
</html>
```